Dentistry on Marlow Marketing Brochure

I require a brochure to market our practice and to send to new patients after they have made initial phone contact, in our 'new patient package' .
My preference is for a double sided A4 trifold brochure.
Please find attached the style guide and information to be included.
Also, please visit our website at www.dentistryonmarlow.com.au to get an idea of our brand- we prefer a clean, fresh look that still conveys warmth and professionalism.
The images from our website can be used for the brochure.
Please include the map attached.

```html
<!DOCTYPE html>
<html lang="en">
<head>
<meta charset="utf-8">
<title>Dentistry on Marlow – Brochure Inside</title>
<link rel="stylesheet" href="https://fonts.googleapis.com/css2?family=Lora:ital,wght@1,400&family=Source+Sans+3:wght@300;400&display=swap">
<style>
  :root {
    --olive: #b3b52a;
    --olive-dark: #a5a722;
    --grey-panel: #e4e4e4;
    --text: #5a5a5a;
    --text-soft: #7a7a7a;
    --white: #ffffff;
    --radius: 48px;
  }
  * { box-sizing: border-box; margin: 0; padding: 0; }
  html, body { width: 1200px; height: 848px; overflow: hidden; background: var(--white); }
  .spread {
    position: relative; width: 1200px; height: 848px; overflow: hidden;
    font-family: "Source Sans 3", "Myriad Pro", Arial, sans-serif;
    font-weight: 400; color: var(--text);
  }
  .photo { position: absolute; }

  /* Left panel */
  .welcome-panel {
    position: absolute; left: 0; top: 172px; width: 400px; height: 676px;
    background: var(--olive);
    border-top-right-radius: var(--radius);
    border-bottom-right-radius: var(--radius);
  }
  .photo--team {
    left: 0; top: 0; width: 400px; height: 178px;
    background: linear-gradient(180deg, #e9ebe8 0%, #cfd2cc 55%, #9fa08c 100%);
    border-bottom-right-radius: var(--radius);
  }
  .welcome-title {
    position: absolute; left: 58px; top: 186px;
    font-family: "Lora", Georgia, serif; font-style: italic; font-weight: 400;
    font-size: 58px; line-height: 1; color: var(--white);
  }
  .welcome-copy {
    position: absolute; left: 60px; top: 248px; width: 312px;
    color: var(--white); font-size: 14.6px; line-height: 19.2px; font-weight: 300;
  }
  .welcome-copy p + p { margin-top: 19px; }

  /* Middle panel */
  .services-panel {
    position: absolute; left: 400px; top: 0; width: 400px; height: 620px;
    background: var(--grey-panel);
  }
  .photo--consult {
    left: 400px; top: 0; width: 400px; height: 178px;
    background: linear-gradient(160deg, #dfe3e6 0%, #b9bfc4 50%, #6d7278 100%);
    border-bottom-left-radius: var(--radius);
    border-bottom-right-radius: var(--radius);
  }
  .photo--scanner {
    left: 400px; top: 602px; width: 400px; height: 246px;
    background: linear-gradient(150deg, #cfdad8 0%, #9fb1b6 45%, #5b6f86 100%);
    border-bottom-right-radius: var(--radius);
  }
  .section-title {
    font-family: "Lora", Georgia, serif; font-style: italic; font-weight: 400;
    font-size: 23px; line-height: 1.1; color: var(--olive);
    letter-spacing: 0.3px;
  }
  .services { position: absolute; left: 432px; top: 222px; width: 340px; }
  .services-list { list-style: none; margin-top: 8px; font-size: 15px; line-height: 21.6px; }
  .services-list .sub { padding-left: 40px; position: relative; }
  .services-list .sub::before {
    content: ""; position: absolute; left: 24px; top: 9px;
    width: 4px; height: 4px; border-radius: 50%; background: var(--text);
  }

  /* Right panel */
  .photo--child {
    left: 800px; top: 0; width: 400px; height: 178px;
    background: linear-gradient(180deg, #f1eeea 0%, #e0d6cb 55%, #c9a990 100%);
    border-bottom-left-radius: var(--radius);
  }
  .kids { position: absolute; left: 836px; top: 222px; width: 304px; }
  .kids-copy { margin-top: 8px; font-size: 14.6px; line-height: 18.9px; }
  .kids-days { margin-top: 26px; }
  .kids-note { margin-top: 14px; font-size: 11.6px; line-height: 14px; color: var(--text-soft); }
</style>
</head>
<body>
<main class="spread">
  <section class="column column--welcome">
    <div class="photo photo--team" role="img" aria-label="Photo of the practice team posing together in the clinic lounge"></div>
    <div class="welcome-panel"></div>
    <h1 class="welcome-title">Welcome</h1>
    <div class="welcome-copy">
      <p>At Dentistry On Marlow we offer an advanced standard of dental care services, using the most current philosophies and techniques. Our practitioners personalise dental care to your individual requirements, not only caring for your teeth and gums, but also caring about your general health and wellbeing.</p>
      <p>We understand that dentistry is about so much more than just healthy teeth and gums. It's also about how you function, your appearance and most importantly, how you feel- giving you confidence to be yourself!</p>
      <p>Our aim is to create and maintain sustainable healthy mouths for life, allowing you to feel comfortable and confident. This is achieved by our commitment to high quality, long lasting dental solutions when required and using preventive solutions for long term stability. Our caring, gentle dentists will take the time to listen to your concerns and help you to achieve your dental goals.</p>
      <p>We are so proud to be able to serve you with a comfortable, state-of-the-art facility and an award winning dental team who have been selected as the most caring, professional and highly respected in their field.</p>
    </div>
  </section>

  <section class="column column--services">
    <div class="services-panel"></div>
    <div class="photo photo--consult" role="img" aria-label="Photo of a dentist reviewing a treatment brochure with a smiling receptionist"></div>
    <div class="services">
      <h2 class="section-title">Our services include:</h2>
      <ul class="services-list">
        <li class="sub">Dental implants</li>
        <li>CERAFIT ceramic restorations</li>
        <li>Restorations</li>
        <li class="sub">Root canal therapy</li>
        <li class="sub">Crown and bridge</li>
        <li class="sub">Veneers</li>
        <li class="sub">Hygiene care</li>
        <li class="sub">Whitening</li>
        <li class="sub">Children's dental care</li>
        <li class="sub">Mouthguards</li>
        <li class="sub">Gum treatment</li>
        <li>Sedation dentistry</li>
        <li>Digital radiographs and OPGs</li>
      </ul>
    </div>
    <div class="photo photo--scanner" role="img" aria-label="Photo of a dentist pointing at a digital tooth scan on a monitor for a patient"></div>
  </section>

  <section class="column column--kids">
    <div class="photo photo--child" role="img" aria-label="Photo of a smiling young girl in the dental chair"></div>
    <div class="kids">
      <h2 class="section-title">Child and Teen Dental</h2>
      <p class="kids-copy">Dental decay rates are rapidly rising. To ensure our young patients have optimum dental health for life, Dentistry on Marlow is investing more time and effort into the care of our children and teenage patients. Our oral health therapists are our children's dental program practitioners, as they are specifically trained in children's dental care.<br>
      Our OHTs have a special interest in the prevention of dental disease throughout the lifespan. They will provide you with the most current advice and product recommendations to suit your individual needs. They are specifically focused on giving your child the best head start they need to maintain a healthy smile for life.</p>

      <h2 class="section-title kids-days">Children's Dental Days</h2>
      <p class="kids-copy">Our children's days are fantastic for young children who haven't been to the dentist before or are shy or nervous about going to the dentist. This is a fun day where children can have their face painted, put on dress ups, get their teeth checked and go home with lots of rewards, a happy smile and a positive dental experience!</p>
      <p class="kids-note">Photos from our previous children's days are available on the Dentistry On Marlow Friendbook page.</p>
    </div>
  </section>
</main>
</body>
</html>
```